Vellmore Quadrant Systems LLC
Elevate Your Workflow
Vellmore Quadrant Systems LLC - Information Technology
Creative Brief
Corporate
Dorian Feltcher
President
Ashford Ridge, VA
dorian@vellmore-quadrant.example
www.vellmore-quadrant.example
Elevate Your Workflow www.vellmore-quadrant.example

```html
<!DOCTYPE html>
<html lang="en">
<head>
<meta charset="utf-8">
<title>Vellmore Quadrant Systems LLC – Business Cards</title>
<link rel="stylesheet" href="https://fonts.googleapis.com/css2?family=Arimo:wght@400;700&display=swap">
<style>
  :root {
    --cyan: #1fb5e4;
    --cyan-faint: #dff2fa;
    --ink: #231f20;
    --dark-card: #2b2728;
    --border: #b9b9b9;
    --page: #ffffff;
    --white: #ffffff;
  }
  * { box-sizing: border-box; margin: 0; padding: 0; }
  html, body { width: 1200px; height: 710px; overflow: hidden; background: var(--page); }
  body { position: relative; font-family: "Arimo", Arial, sans-serif; color: var(--ink); }

  .card { position: absolute; width: 568px; height: 312px; overflow: hidden; }
  .card--front { left: 19px; top: 30px; background: var(--white); border: 2px solid var(--border); }
  .card--cyan { left: 607px; top: 30px; background: var(--cyan); }
  .card--white { left: 19px; top: 362px; background: var(--white); border: 2px solid var(--border); }
  .card--dark { left: 607px; top: 362px; background: var(--dark-card); }

  .brand { position: absolute; display: flex; align-items: center; gap: 12px; }
  .brand__mark { flex: none; background: var(--cyan); border-radius: 6px; }
  .brand__name { font-weight: 700; line-height: 1.05; letter-spacing: -0.3px; }
  .brand__tagline { position: absolute; font-size: 13px; font-weight: 400; }

  /* front */
  .card--front .brand { left: 24px; top: 18px; }
  .card--front .brand__mark { width: 60px; height: 48px; }
  .card--front .brand__name { font-size: 22px; color: var(--ink); width: 200px; }
  .card--front .brand__tagline { left: 96px; top: 78px; color: var(--ink); }
  .rule-black { position: absolute; left: 318px; right: -2px; top: 18px; height: 9px; background: var(--ink); }
  .rule-cyan { position: absolute; left: 318px; right: -2px; top: 31px; height: 3px; background: var(--cyan); }
  .person { position: absolute; left: 180px; top: 140px; text-align: center; width: 200px; }
  .person__name { font-size: 22px; color: var(--cyan); }
  .person__title { font-size: 12px; margin-top: 4px; }
  .decor { position: absolute; left: 395px; top: 168px; width: 150px; height: 110px; background: var(--cyan-faint); border-radius: 10px; }
  .contact { position: absolute; left: 10px; bottom: 14px; font-size: 12.5px; line-height: 16px; }
  .contact .web { color: var(--cyan); }

  /* backs */
  .back .brand { left: 50%; transform: translateX(-50%); top: 84px; }
  .back .brand__mark { width: 92px; height: 74px; }
  .back .brand__name { font-size: 30px; width: 270px; }
  .back .brand__tagline { left: 104px; top: 100%; margin-top: 6px; white-space: nowrap; }
  .card--cyan .brand__mark { background: var(--white); }
  .card--cyan .brand__name,
  .card--cyan .brand__tagline { color: var(--ink); }
  .card--white .brand { top: 60px; }
  .card--white .brand__mark { width: 110px; height: 88px; }
  .card--white .brand__name { font-size: 36px; width: 330px; color: var(--ink); }
  .card--white .brand__tagline { left: 122px; font-size: 17px; color: var(--ink); }
  .card--dark .brand__name,
  .card--dark .brand__tagline { color: var(--white); }

  .web-line { position: absolute; left: 0; right: 0; bottom: 40px; text-align: center; font-size: 19px; }
  .card--cyan .web-line,
  .card--white .web-line { color: var(--ink); }
  .card--dark .web-line { color: var(--white); }
</style>
</head>
<body>

<section class="card card--front" aria-label="Card front">
  <div class="brand">
    <span class="brand__mark"></span>
    <span class="brand__name">Vellmore Quadrant Systems LLC</span>
  </div>
  <span class="brand__tagline">Elevate Your Workflow.</span>
  <div class="rule-black"></div>
  <div class="rule-cyan"></div>
  <div class="decor" role="img" aria-label="Faint background square"></div>
  <div class="person">
    <p class="person__name">Dorian Feltcher</p>
    <p class="person__title">President</p>
  </div>
  <div class="contact">
    <p>Ashford Ridge, VA</p>
    <p>Cell: 202.555.0147</p>
    <p>Email: dorian@vellmore-quadrant.example</p>
    <p class="web">www.vellmore-quadrant.example</p>
  </div>
</section>

<section class="card card--cyan back" aria-label="Card back, cyan">
  <div class="brand">
    <span class="brand__mark"></span>
    <span class="brand__name">Vellmore Quadrant Systems LLC</span>
    <span class="brand__tagline">Elevate Your Workflow.</span>
  </div>
  <p class="web-line">www.vellmore-quadrant.example</p>
</section>

<section class="card card--white back" aria-label="Card back, white">
  <div class="brand">
    <span class="brand__mark"></span>
    <span class="brand__name">Vellmore Quadrant Systems LLC</span>
    <span class="brand__tagline">Elevate Your Workflow.</span>
  </div>
  <p class="web-line">www.vellmore-quadrant.example</p>
</section>

<section class="card card--dark back" aria-label="Card back, dark">
  <div class="brand">
    <span class="brand__mark"></span>
    <span class="brand__name">Vellmore Quadrant Systems LLC</span>
    <span class="brand__tagline">Elevate Your Workflow.</span>
  </div>
  <p class="web-line">www.vellmore-quadrant.example</p>
</section>

</body>
</html>
```